VELINTA Promotions - Business Card Design Project

We are looking for a classy business cards for Promotion Company based in Toronto, Canada named Velinta Promotions.

Velinta Promotions has an idea and vision to set high standard, be EXCLUSIVE and attract a group of people that will follow us through events we promote (night clubs, brand promotions, music events, and sport events)

We want to present a high standards and classy image to the others...
Updates

Target Market(s)

male/female age 25-40 Target: business owners young entrepreneur - clubing industry - media industry - promotion industry - marketing media industry

Industry/Entity Type

Events

Requirements
Must have
• business cards should be classy, make people feel exclusive , make people react ..

```html
<!DOCTYPE html>
<html lang="en">
<head>
<meta charset="utf-8">
<title>Velinta Promotions – Business Card</title>
<link href="https://fonts.googleapis.com/css2?family=Didact+Gothic&display=swap" rel="stylesheet">
<style>
  :root {
    --page: #ffffff;
    --card: #000000;
    --band: #5e5e5e;
    --brand: #1ab2e8;
    --ink-light: #ffffff;
    --ink-dark: #000000;
    --shadow: rgba(0, 0, 0, 0.55);
  }
  html, body {
    margin: 0;
    padding: 0;
    width: 1200px;
    height: 1200px;
    overflow: hidden;
    background: var(--page);
    font-family: "Didact Gothic", "Century Gothic", sans-serif;
  }
  .canvas {
    position: relative;
    width: 1200px;
    height: 1200px;
  }
  .card {
    position: absolute;
    left: 208px;
    width: 472px;
    height: 334px;
    background: var(--card);
    box-shadow: 8px 8px 6px var(--shadow);
    overflow: hidden;
  }
  .card--back { top: 270px; }
  .card--front { top: 667px; }

  .side-label {
    position: absolute;
    margin: 0;
    font-size: 29px;
    font-weight: 700;
    letter-spacing: 2px;
    color: var(--ink-dark);
  }
  .side-label--back { left: 721px; top: 451px; }
  .side-label--front { left: 728px; top: 781px; }

  /* brand name */
  .brand {
    position: absolute;
    color: var(--brand);
    line-height: 1;
    text-align: right;
  }
  .brand__name { display: block; }
  .brand__sub { display: block; }

  .brand--small { left: 22px; top: 22px; }
  .brand--small .brand__name { font-size: 20px; letter-spacing: 1px; }
  .brand--small .brand__sub { font-size: 6px; letter-spacing: 2.5px; margin-top: 1px; }

  .brand--large { left: 0; right: 0; top: 140px; text-align: center; }
  .brand--large .brand__name { font-size: 46px; letter-spacing: 3px; }
  .brand--large .brand__sub { font-size: 11px; letter-spacing: 7px; margin-top: 4px; padding-left: 90px; }

  /* back side */
  .band {
    position: absolute;
    left: 0;
    top: 0;
    width: 472px;
    height: 334px;
  }
  .band path { fill: var(--band); }

  .holder {
    position: absolute;
    left: 0;
    right: 0;
    top: 128px;
    text-align: center;
    color: var(--ink-light);
  }
  .holder__name {
    display: inline-block;
    margin: 0;
    padding: 0 12px 2px;
    font-size: 22px;
    font-weight: 400;
    letter-spacing: 2.5px;
    border-bottom: 1px solid var(--ink-light);
  }
  .holder__role {
    margin: 3px 0 0;
    font-size: 13px;
    letter-spacing: 1px;
  }

  .contact {
    position: absolute;
    left: 15px;
    top: 244px;
    margin: 0;
    padding: 0;
    list-style: none;
    color: var(--ink-light);
    font-size: 10px;
    line-height: 12.3px;
    letter-spacing: 0.6px;
  }

  .services {
    position: absolute;
    left: 0;
    right: 0;
    top: 310px;
    margin: 0;
    padding: 0;
    list-style: none;
    display: flex;
    justify-content: center;
    gap: 5px;
    color: var(--ink-light);
    font-size: 10px;
    letter-spacing: 0.6px;
  }
  .services li + li::before {
    content: "";
    display: inline-block;
    width: 5px;
    height: 5px;
    margin-right: 6px;
    border-radius: 50%;
    background: var(--ink-light);
    vertical-align: 1px;
  }
</style>
</head>
<body>
<main class="canvas">

  <section class="card card--back" aria-label="Business card, back">
    <svg class="band" viewBox="0 0 472 334" aria-hidden="true">
      <path d="M0 180 Q 230 300 472 212 L472 334 L0 334 Z"/>
    </svg>
    <div class="brand brand--small">
      <span class="brand__name">VELINTA</span>
      <span class="brand__sub">PROMOTIONS</span>
    </div>
    <div class="holder">
      <h2 class="holder__name">YOUR NAME</h2>
      <p class="holder__role">Position</p>
    </div>
    <ul class="contact">
      <li>Address:</li>
      <li>Office:</li>
      <li>Telp:</li>
      <li>Email:</li>
    </ul>
    <ul class="services">
      <li>Night Clubs</li>
      <li>Brand Promotions</li>
      <li>Music Events</li>
      <li>Sport Events</li>
    </ul>
  </section>
  <p class="side-label side-label--back">Back</p>

  <section class="card card--front" aria-label="Business card, front">
    <div class="brand brand--large">
      <span class="brand__name">VELINTA</span>
      <span class="brand__sub">PROMOTIONS</span>
    </div>
  </section>
  <p class="side-label side-label--front">Front</p>

</main>
</body>
</html>
```